Valduro.com needs a Mobile FIRST Site

Valduro.com is an insurance broker based in Panama City, Panama that plans to sell car and motorcycle insurance online.

We need to design a total of 5 pages (two of those are A/B test pages). The site will be responsive and will be programmed in React. We will be using Brisk Widget´s library to code Valduro.com. Keep in mind that we are using Brisk Widget to program the site´s functions, not to create the "look and feel" of the site, that is obviously your job. You can learn more about Brisk Widget here... https://brisk-widget.example/

We have created wireframes for the app. Please follow and keep in mind the instructions in the wireframes. You can change things here and there as long as the core functions and goals stay intact. We have uploaded the wireframes along with the company logo and color.

We are planning to A/B test the site´s home page so we need to design two homepages. You can find homepage A and B in the wireframes provided.

We speak Spanish in Panama but you can design the site in English. We can change the text once we receive the designs.

Target Market(s)

25-45 year olds who own a car or motorcylcle and own a credit card.

Industry/Entity Type

Insurance

Font styles to use
Sans Serif

Requirements
Must have
• Follow the wireframes provided and the logo colors.
Nice to have
• Please look at the Image I´ve uploaded from DeskHaven, use it as reference to create HomePage A.

```html
<!DOCTYPE html>
<html lang="en">
<head>
<meta charset="utf-8">
<title>Valduro – Choose insurance</title>
<link href="https://fonts.googleapis.com/css2?family=Mulish:wght@400;600;700;800&display=swap" rel="stylesheet">
<style>
  :root{
    --purple:#44307f;
    --purple-dark:#3b2872;
    --page-bg:#eeeeee;
    --step-bg:#ececec;
    --card-bg:#ffffff;
    --divider:#e6e6e6;
    --ink:#1d1d1f;
    --muted:#2e2e2e;
    --logo-tile:#eeeeee;
  }
  *{box-sizing:border-box;margin:0;padding:0}
  ol,ul,li{list-style:none}
  html,body{width:1200px;height:900px;overflow:hidden;background:var(--page-bg);font-family:"Mulish",sans-serif;color:var(--ink)}
  .screen{position:absolute;left:353px;top:15px;width:494px;height:871px;background:var(--step-bg);overflow:hidden}

  .app-header{height:91px;background:var(--purple);color:#fff;position:relative}
  .status-bar{height:34px;display:flex;align-items:center;padding:0 10px;font-size:15px;position:relative}
  .status-bar .signal{display:flex;gap:2px;margin-right:6px}
  .status-bar .signal i{width:6px;height:6px;border-radius:50%;background:#fff;display:block}
  .status-bar .carrier{margin-left:6px}
  .status-bar .time{position:absolute;left:50%;transform:translateX(-50%)}
  .status-bar .battery{margin-left:auto;display:flex;align-items:center;gap:5px}
  .battery-cell{width:30px;height:12px;border:1px solid #fff;border-radius:2px;padding:1px;position:relative}
  .battery-cell::before{content:"";display:block;width:100%;height:100%;background:#fff}
  .battery-cell::after{content:"";position:absolute;right:-4px;top:3px;width:2px;height:5px;background:#fff}
  .nav-bar{height:57px;display:flex;align-items:center;justify-content:center;position:relative}
  .menu-btn{position:absolute;left:15px;top:18px}
  .brand{font-weight:800;font-size:27px;letter-spacing:-.3px}
  .cart-btn{position:absolute;right:20px;top:16px}

  .stepper{height:78px;display:flex;align-items:center;padding-left:37px;font-size:19px;color:#2b2b2b}
  .step{display:flex;align-items:center;gap:14px;white-space:nowrap}
  .step-num{width:29px;height:29px;border:2px solid #333;border-radius:50%;display:flex;align-items:center;justify-content:center;font-size:17px}
  .step.done{color:var(--purple)}
  .step-line{width:60px;height:1.5px;background:#444;margin:0 8px 0 10px}
  .step.done+.step-line{background:var(--purple)}

  .offer-card{position:relative;height:236px;background:var(--card-bg);border-bottom:1px solid var(--divider)}
  .insurer-tile{position:absolute;left:25px;top:23px;width:74px;height:74px;background:var(--logo-tile);display:flex;align-items:center;justify-content:center;color:var(--purple);font-weight:800;font-size:24px}
  .offer-name{position:absolute;left:122px;top:26px;font-size:20px;font-weight:700;color:var(--purple)}
  .offer-price{position:absolute;left:122px;top:55px;font-size:27px;font-weight:400}
  .buy-btn{position:absolute;left:366px;top:38px;width:103px;height:41px;border-radius:21px;background:var(--purple);color:#fff;font-size:15px;font-weight:600;display:flex;align-items:center;justify-content:center;letter-spacing:.2px}
  .coverage{position:absolute;top:119px;font-size:15px}
  .coverage .label{color:var(--purple);display:block}
  .coverage .amount{display:block;font-size:18px;margin-top:4px}
  .col-1{left:25px}.col-2{left:185px}.col-3{left:347px}
  .perk{position:absolute;top:172px;display:flex;align-items:center;gap:10px;font-size:14.5px;line-height:18px;color:var(--muted)}

  .filter-bar{position:absolute;left:0;right:0;top:811px;height:60px;background:#fff;border-top:1px solid var(--divider);display:flex}
  .filter{flex:1;display:flex;align-items:center;padding:0 26px 0 28px;color:var(--purple);font-size:21px;font-weight:600;gap:14px}
  .filter+.filter{border-left:1px solid var(--divider)}
  .filter .chev{margin-left:auto}
  .currency{font-size:25px;font-weight:800}
</style>
</head>
<body>
<main class="screen">
  <header class="app-header">
    <div class="status-bar">
      <span class="signal"><i></i><i></i><i></i><i></i><i></i></span>
      <svg width="16" height="12" viewBox="0 0 16 12"><path d="M1 4a10 10 0 0 1 14 0M3.5 6.5a6.5 6.5 0 0 1 9 0M6 9a3 3 0 0 1 4 0" stroke="#fff" stroke-width="1.6" fill="none" stroke-linecap="round"/><circle cx="8" cy="11" r="1" fill="#fff"/></svg>
      <span class="carrier">Kelto UZB</span>
      <span class="time">9:41 AM</span>
      <span class="battery">100% <span class="battery-cell"></span></span>
    </div>
    <nav class="nav-bar">
      <svg class="menu-btn" width="26" height="20" viewBox="0 0 26 20"><path d="M0 2h26M0 10h26M0 18h26" stroke="#fff" stroke-width="2"/></svg>
      <span class="brand">Valduro.com</span>
      <svg class="cart-btn" width="28" height="24" viewBox="0 0 28 24"><path d="M1 4h3l3 11h12l2-8H6" stroke="#fff" stroke-width="1.8" fill="none" stroke-linejoin="round"/><path d="M9 9h10M10 12h8" stroke="#fff" stroke-width="1.4"/><circle cx="9" cy="19" r="1.8" fill="#fff"/><circle cx="17" cy="19" r="1.8" fill="#fff"/><circle cx="22" cy="5" r="5" fill="#6b57c4"/><text x="22" y="8" font-size="8" font-family="Mulish,sans-serif" font-weight="700" fill="#fff" text-anchor="middle">2</text></svg>
    </nav>
  </header>

  <div class="stepper" role="list">
    <div class="step done" role="listitem">
      <svg width="30" height="30" viewBox="0 0 30 30"><circle cx="15" cy="15" r="15" fill="var(--purple)"/><path d="M9 15.5l4 4 8-8" stroke="#fff" stroke-width="2.4" fill="none" stroke-linecap="round" stroke-linejoin="round"/></svg>
      Elige
    </div>
    <span class="step-line"></span>
    <div class="step" role="listitem"><span class="step-num">2</span>Datos</div>
    <span class="step-line"></span>
    <div class="step" role="listitem"><span class="step-num">3</span>Paga</div>
  </div>

  <section class="offer-list">
    <article class="offer-card">
      <div class="insurer-tile">AS</div>
      <h2 class="offer-name">Name of Insurance</h2>
      <p class="offer-price">$10,000</p>
      <span class="buy-btn">BUY NOW</span>
      <p class="coverage col-1"><span class="label">insurance coverage</span><span class="amount">$7,000</span></p>
      <p class="coverage col-2"><span class="label">accident coverage</span><span class="amount">$5,000</span></p>
      <p class="coverage col-3"><span class="label">other coverage</span><span class="amount">$4,000</span></p>
      <div class="perk col-1"><svg width="39" height="39" viewBox="0 0 40 40"><path d="M20 1l5 4 6-1 2 6 5 4-2 6 2 6-5 4-2 6-6-1-5 4-5-4-6 1-2-6-5-4 2-6-2-6 5-4 2-6 6 1z" fill="var(--purple)"/><path d="M13 20.5l5 5 9-10" stroke="#fff" stroke-width="2.6" fill="none" stroke-linecap="round" stroke-linejoin="round"/></svg><span>trusted<br>insurance</span></div>
      <div class="perk col-2"><svg width="39" height="39" viewBox="0 0 40 40"><circle cx="20" cy="20" r="18" stroke="var(--purple)" stroke-width="2.6" fill="none"/><text x="20" y="26" font-size="17" font-weight="800" font-family="Mulish,sans-serif" fill="var(--purple)" text-anchor="middle">($)</text></svg><span>money back<br>guarantee</span></div>
      <div class="perk col-3"><svg width="32" height="38" viewBox="0 0 32 38"><path d="M16 1l14 5v11c0 10-7 17-14 20C9 34 2 27 2 17V6z" fill="var(--purple)"/><path d="M16 5v14H6V9l10-4z" fill="#fff"/><path d="M16 19h10c-1 7-5 12-10 14z" fill="#fff"/></svg><span>full<br>protection</span></div>
    </article>

    <article class="offer-card">
      <div class="insurer-tile">AB</div>
      <h2 class="offer-name">Name of Insurance</h2>
      <p class="offer-price">$10,000</p>
      <span class="buy-btn">BUY NOW</span>
      <p class="coverage col-1"><span class="label">insurance coverage</span><span class="amount">$7,000</span></p>
      <p class="coverage col-2"><span class="label">accident coverage</span><span class="amount">$5,000</span></p>
      <p class="coverage col-3"><span class="label">other coverage</span><span class="amount">$4,000</span></p>
      <div class="perk col-1"><svg width="39" height="39" viewBox="0 0 40 40"><path d="M20 1l5 4 6-1 2 6 5 4-2 6 2 6-5 4-2 6-6-1-5 4-5-4-6 1-2-6-5-4 2-6-2-6 5-4 2-6 6 1z" fill="var(--purple)"/><path d="M13 20.5l5 5 9-10" stroke="#fff" stroke-width="2.6" fill="none" stroke-linecap="round" stroke-linejoin="round"/></svg><span>trusted<br>insurance</span></div>
      <div class="perk col-2"><svg width="39" height="39" viewBox="0 0 40 40"><circle cx="20" cy="20" r="18" stroke="var(--purple)" stroke-width="2.6" fill="none"/><text x="20" y="26" font-size="17" font-weight="800" font-family="Mulish,sans-serif" fill="var(--purple)" text-anchor="middle">($)</text></svg><span>money back<br>guarantee</span></div>
      <div class="perk col-3"><svg width="32" height="38" viewBox="0 0 32 38"><path d="M16 1l14 5v11c0 10-7 17-14 20C9 34 2 27 2 17V6z" fill="var(--purple)"/><path d="M16 5v14H6V9l10-4z" fill="#fff"/><path d="M16 19h10c-1 7-5 12-10 14z" fill="#fff"/></svg><span>full<br>protection</span></div>
    </article>

    <article class="offer-card">
      <div class="insurer-tile">CD</div>
      <h2 class="offer-name">Name of Insurance</h2>
      <p class="offer-price">$10,000</p>
      <span class="buy-btn">BUY NOW</span>
      <p class="coverage col-1"><span class="label">insurance coverage</span><span class="amount">$7,000</span></p>
      <p class="coverage col-2"><span class="label">accident coverage</span><span class="amount">$5,000</span></p>
      <p class="coverage col-3"><span class="label">other coverage</span><span class="amount">$4,000</span></p>
    </article>
  </section>

  <footer class="filter-bar">
    <div class="filter">
      <svg width="48" height="20" viewBox="0 0 48 20"><path d="M2 14v-4l6-2 7-5h14l9 5 7 1 1 5h-4M10 14H2M36 14H16" stroke="var(--purple)" stroke-width="2" fill="none" stroke-linejoin="round"/><circle cx="13" cy="14" r="3.5" stroke="var(--purple)" stroke-width="2" fill="#fff"/><circle cx="39" cy="14" r="3.5" stroke="var(--purple)" stroke-width="2" fill="#fff"/><path d="M16 8h20l-6-4H19z" fill="var(--purple)"/></svg>
      Car
      <svg class="chev" width="16" height="11" viewBox="0 0 16 11"><path d="M2 2l6 6 6-6" stroke="var(--purple)" stroke-width="3" fill="none"/></svg>
    </div>
    <div class="filter">
      <span class="currency">€</span>
      Low to High
      <svg class="chev" width="16" height="11" viewBox="0 0 16 11"><path d="M2 2l6 6 6-6" stroke="var(--purple)" stroke-width="3" fill="none"/></svg>
    </div>
  </footer>
</main>
</body>
</html>
```